I am looking for a business card design with the following info:

*I need the design to be in two sides one in English and the other in Arabic, and I want it horizontal design.
Please note that each side has to have the same information but one in English and the other in Arabic

Company Name: Wafir and وافر
Company Logo: Attached.
Company Activity: E rental cars And لخدمات تأجير السيارات الالكترونية
Company Snapchat: Dorqanet
Instagram Account: Dorqanet
Facebook Account: Dorqanet
Name: Tamer and تامر
Title: Manager and مدير
Location: Saudi Arabia - Riyadh and المملكة العربية السعودية - الرياض
Email : contact@wafir-rentals.example
Website: www.wafir-rentals.example
Mob #: +966-501234876
Tel #: +966-117654321

The design has to be in three colors only (Green, Black and White)

```html
<!DOCTYPE html>
<html lang="en">
<head>
<meta charset="utf-8">
<title>Wafir Business Card – English and Arabic Sides</title>
<link href="https://fonts.googleapis.com/css2?family=Poppins:wght@400;500;600;700&family=Cairo:wght@400;600;700;800&display=swap" rel="stylesheet">
<style>
  :root {
    --green: #2db84b;
    --ink: #3a3a3a;
    --paper: #ffffff;
    --rule: #c4c4c4;
    --backdrop: #2a2a2a;
  }
  * { box-sizing: border-box; margin: 0; padding: 0; }
  html, body { width: 1200px; height: 900px; overflow: hidden; }
  body {
    background: var(--backdrop);
    font-family: "Poppins", sans-serif;
    position: relative;
  }
  .card {
    position: absolute;
    left: 240px;
    width: 720px;
    height: 400px;
    background: var(--paper);
    overflow: hidden;
  }
  .card--english { top: 35px; }
  .card--arabic { top: 465px; }
  .card-frame { position: absolute; inset: 0; }

  .brand-mark {
    position: absolute;
    left: 60px;
    top: 130px;
    width: 250px;
    text-align: center;
  }
  .brand-mark__row {
    display: flex;
    align-items: center;
    justify-content: center;
    gap: 12px;
  }
  .brand-mark__dot {
    width: 56px; height: 56px;
    border-radius: 50%;
    background: var(--green);
  }
  .brand-mark__name {
    font-weight: 700;
    font-size: 36px;
    color: var(--green);
    line-height: 1;
  }
  .holder-name {
    margin-top: 14px;
    font-weight: 700;
    font-size: 30px;
    color: var(--green);
    line-height: 1;
  }
  .holder-title {
    font-size: 17px;
    color: var(--ink);
    margin-top: 2px;
  }

  .divider {
    position: absolute;
    left: 340px;
    top: 115px;
    width: 1px;
    height: 175px;
    background: var(--rule);
  }

  .info {
    position: absolute;
    left: 385px;
    top: 42px;
    width: 290px;
  }
  .social {
    display: flex;
    align-items: center;
    gap: 7px;
    font-weight: 700;
    font-size: 14px;
    color: var(--ink);
  }
  .social__dot {
    width: 13px; height: 13px;
    border-radius: 50%;
    background: var(--green);
  }
  .social__handle { margin-left: 4px; }
  .company-name {
    margin-top: 6px;
    font-weight: 700;
    font-size: 30px;
    color: var(--green);
    line-height: 1.05;
  }
  .company-activity {
    font-size: 17px;
    color: var(--ink);
    line-height: 1.2;
  }
  .contacts {
    list-style: none;
    margin-top: 20px;
  }
  .contacts li {
    display: flex;
    align-items: center;
    gap: 10px;
    font-weight: 600;
    font-size: 13px;
    color: var(--green);
    height: 24px;
  }
  .contacts svg { width: 15px; height: 15px; flex: none; fill: var(--green); }

  .card--arabic .info { top: 48px; }
  .card--arabic .arabic,
  .arabic { font-family: "Cairo", sans-serif; direction: rtl; }
  .card--arabic .holder-block { text-align: left; margin-top: 4px; }
  .card--arabic .holder-block .name-ar {
    font-family: "Cairo", sans-serif;
    font-weight: 800;
    font-size: 30px;
    color: var(--green);
    line-height: 1.1;
  }
  .card--arabic .holder-block .title-ar {
    font-family: "Cairo", sans-serif;
    font-weight: 600;
    font-size: 16px;
    color: var(--ink);
    line-height: 1.1;
  }
  .card--arabic .contacts { margin-top: 30px; }
  .card--arabic .brand-mark { top: 120px; left: 40px; width: 290px; }
  .card--arabic .brand-mark__name { font-family: "Cairo", sans-serif; font-weight: 800; }
  .company-activity-ar {
    margin-top: 14px;
    font-family: "Cairo", sans-serif;
    font-weight: 600;
    font-size: 18px;
    color: var(--ink);
  }
</style>
</head>
<body>

<!-- English side -->
<section class="card card--english">
  <svg class="card-frame" viewBox="0 0 720 400" aria-hidden="true">
    <polygon fill="var(--green)" points="0,0 250,0 218,30 30,30 30,250 0,285"/>
    <polygon fill="var(--green)" points="720,400 720,130 690,165 690,370 470,370 440,400"/>
  </svg>

  <div class="brand-mark">
    <div class="brand-mark__row">
      <span class="brand-mark__dot"></span>
      <span class="brand-mark__name">Wafir</span>
    </div>
    <div class="holder-name">Tamer</div>
    <div class="holder-title">Manager</div>
  </div>

  <div class="divider"></div>

  <div class="info">
    <div class="social">
      <span class="social__dot"></span>
      <span class="social__dot"></span>
      <span class="social__dot"></span>
      <span class="social__handle">Dorqanet</span>
    </div>
    <div class="company-name">Wafir</div>
    <div class="company-activity">E rental cars</div>
    <ul class="contacts">
      <li><svg viewBox="0 0 24 24"><path d="M6.6 10.8a15.1 15.1 0 0 0 6.6 6.6l2.2-2.2a1 1 0 0 1 1-.25 11.4 11.4 0 0 0 3.6.57 1 1 0 0 1 1 1V20a1 1 0 0 1-1 1A17 17 0 0 1 3 4a1 1 0 0 1 1-1h3.5a1 1 0 0 1 1 1c0 1.25.2 2.45.57 3.57a1 1 0 0 1-.25 1z"/></svg>+966-117654321</li>
      <li><svg viewBox="0 0 24 24"><path d="M7 2h10a2 2 0 0 1 2 2v16a2 2 0 0 1-2 2H7a2 2 0 0 1-2-2V4a2 2 0 0 1 2-2zm0 3v13h10V5zm5 14.2a1 1 0 1 0 0 .01z"/></svg>+966-501234876</li>
      <li><svg viewBox="0 0 24 24"><path d="M2 5h20v14H2zm2 2v.4l8 5.2 8-5.2V7zm0 2.8V17h16V9.8l-8 5.2z"/></svg>contact@wafir-rentals.example</li>
      <li><svg viewBox="0 0 24 24"><path d="M12 2a10 10 0 1 0 0 20 10 10 0 0 0 0-20zm6.9 9h-3a15 15 0 0 0-1.3-6 8 8 0 0 1 4.3 6zM12 4.1c.9 1.3 1.8 3.6 1.9 6.9h-3.8c.1-3.3 1-5.6 1.9-6.9zM9.4 5a15 15 0 0 0-1.3 6h-3a8 8 0 0 1 4.3-6zM5.1 13h3a15 15 0 0 0 1.3 6 8 8 0 0 1-4.3-6zm6.9 6.9c-.9-1.3-1.8-3.6-1.9-6.9h3.8c-.1 3.3-1 5.6-1.9 6.9zm2.6-.9a15 15 0 0 0 1.3-6h3a8 8 0 0 1-4.3 6z"/></svg>www.wafir-rentals.example</li>
      <li><svg viewBox="0 0 24 24"><path d="M12 2a7 7 0 0 0-7 7c0 5.2 7 13 7 13s7-7.8 7-13a7 7 0 0 0-7-7zm0 9.5A2.5 2.5 0 1 1 12 6.5a2.5 2.5 0 0 1 0 5z"/></svg>Saudi Arabia - Riyadh</li>
    </ul>
  </div>
</section>

<!-- Arabic side -->
<section class="card card--arabic" lang="ar">
  <svg class="card-frame" viewBox="0 0 720 400" aria-hidden="true">
    <polygon fill="var(--green)" points="0,0 250,0 218,30 30,30 30,250 0,285"/>
    <polygon fill="var(--green)" points="720,400 720,130 690,165 690,370 470,370 440,400"/>
  </svg>

  <div class="brand-mark">
    <div class="brand-mark__row">
      <span class="brand-mark__dot"></span>
      <span class="brand-mark__name arabic">وافر</span>
    </div>
    <div class="company-activity-ar arabic">لخدمات تأجير السيارات الالكترونية</div>
  </div>

  <div class="divider"></div>

  <div class="info">
    <div class="social">
      <span class="social__dot"></span>
      <span class="social__dot"></span>
      <span class="social__dot"></span>
      <span class="social__handle">Dorqanet</span>
    </div>
    <div class="holder-block">
      <div class="name-ar arabic">تامر</div>
      <div class="title-ar arabic">مدير</div>
    </div>
    <ul class="contacts">
      <li><svg viewBox="0 0 24 24"><path d="M6.6 10.8a15.1 15.1 0 0 0 6.6 6.6l2.2-2.2a1 1 0 0 1 1-.25 11.4 11.4 0 0 0 3.6.57 1 1 0 0 1 1 1V20a1 1 0 0 1-1 1A17 17 0 0 1 3 4a1 1 0 0 1 1-1h3.5a1 1 0 0 1 1 1c0 1.25.2 2.45.57 3.57a1 1 0 0 1-.25 1z"/></svg>+966-117654321</li>
      <li><svg viewBox="0 0 24 24"><path d="M7 2h10a2 2 0 0 1 2 2v16a2 2 0 0 1-2 2H7a2 2 0 0 1-2-2V4a2 2 0 0 1 2-2zm0 3v13h10V5zm5 14.2a1 1 0 1 0 0 .01z"/></svg>+966-501234876</li>
      <li><svg viewBox="0 0 24 24"><path d="M2 5h20v14H2zm2 2v.4l8 5.2 8-5.2V7zm0 2.8V17h16V9.8l-8 5.2z"/></svg>contact@wafir-rentals.example</li>
      <li><svg viewBox="0 0 24 24"><path d="M12 2a10 10 0 1 0 0 20 10 10 0 0 0 0-20zm6.9 9h-3a15 15 0 0 0-1.3-6 8 8 0 0 1 4.3 6zM12 4.1c.9 1.3 1.8 3.6 1.9 6.9h-3.8c.1-3.3 1-5.6 1.9-6.9zM9.4 5a15 15 0 0 0-1.3 6h-3a8 8 0 0 1 4.3-6zM5.1 13h3a15 15 0 0 0 1.3 6 8 8 0 0 1-4.3-6zm6.9 6.9c-.9-1.3-1.8-3.6-1.9-6.9h3.8c-.1 3.3-1 5.6-1.9 6.9zm2.6-.9a15 15 0 0 0 1.3-6h3a8 8 0 0 1-4.3 6z"/></svg>www.wafir-rentals.example</li>
      <li><svg viewBox="0 0 24 24"><path d="M12 2a7 7 0 0 0-7 7c0 5.2 7 13 7 13s7-7.8 7-13a7 7 0 0 0-7-7zm0 9.5A2.5 2.5 0 1 1 12 6.5a2.5 2.5 0 0 1 0 5z"/></svg><span class="arabic">المملكة العربية السعودية - الرياض</span></li>
    </ul>
  </div>
</section>

</body>
</html>
```